Colourful Bold Design for Pet Insurance Website

PLEASE NOTE THAT THIS PROJECT HAS BEEN EXTENDED. Please read the PROJECT EXTENSION DOCUMENT BEFORE STARTING WORK ON ANY DESIGNS.

We are looking for a colourful bold new template design for our JOOMLA HOMEPAGE and a matching design for our new WORDPRESS BLOG.

The website will help pet owners work out which insurance policy best meets their needs. The aim of the website is to explain policy differences in a plain clear manner.

The website will need to have a professional colourful image. It needs to be BOLD, CLEAN AND SHARP rather than soft, pastel and cuddly.

COLOUR SCHEME
The website needs to have a bold colourful design on a white background.
On the inner pages we will have five different types of policies which will be colour coded. We would ideally therefore like to incorporate five distinct colours in the design. See attached document for example of colour schemes we like.

LOGO
We want to keep the existing logo. Please find the file attached. You may though change the logo colours.

CONTENT
One of the reasons for the new design is that we want to change the style of the homepage and include new content. Our current homepage can be found at www.cover-compare-quizzo.co.uk.

Content Required
Slideshow
Article Intro.. About Pet Insurance
Policy Lookup Box (see existing site… you can change the design of this)
Six link options (see links on left of current page)
Latest Reviews (List of 6)
Ad (Same dimensions as currently on homepage)

News and Comment Section - To include Three or Four Articles, Title, Intro to article (probably 3 or 4 lines .. about 400px wide), Read more link
Social Media Section
Friendwall Plugin with Feed
Latest Tweets Plugin
Pet Charities Latest Tweets
Footer
Larger footer with lots of links grouped in sections

It does not need to include the clipart pic of the pets which is on the current homepage.

Examples of Websites and Templates We Like
http://www.brindlevox.com/ (like colours… fonts…layout)
http://layoutdemo.quarnofield.com/?template=elated&path=/... (like the clarity, "white" space etc)
http://www.skellpravo.com/demo/58817.html (like white space, clear easy to read fonts… don’t like colour scheme, size of top picture)
http://www.skellpravo.com/website-templates/62391.html (like colour scheme, use of white space)

FEEDBACK
I will provide lots of feedback on all designs submitted so that together we can get the best result.

For clarification this is a DESIGN ONLY project. Our website developer will view the designs before we make our final choice as he wants to ensure he can develop "sharp, practical and most importantly light weight web interface" from the design.

Just updated this brief to clarify design issues, content issues and to give some more examples of site designs I like. 

Please note that although we wish to keep the logo you can change the colours to suit your design. 

Please note that we have now added details of pictures we would be happy to use on the website.  We would prefer it if you used one of these.   Otherwise please ensure your picture includes a nice dog and nice cat and no people!

I have been delighted with the quality of the designs submitted for this project.  So much so that I am going to extend the project to include some additional inner pages.   The amended brief will be posted on here on Friday 10 May.   The deadline will be extended and the budget will also be increased. 

Reason: Additional inner pages now required. Budget will be increased. Revised brief to be posted on here Friday 10 May.

Target Market(s)

Pet owners in the UK who are confused about pet insurance. It therefore needs to be a bold design which is plain, clean and easy to read. It should use bold colours rather than pastels and should not use "cuddly" images.

Industry/Entity Type

Insurance

Requirements
Must have
• Bold clear and distinct colours (preferably 5)
Content as per uploaded file (not just content from existing site)
Easy to read fonts
Should not have
• Pastel colours
Cuddly images

```html
<!DOCTYPE html>
<html lang="en">
<head>
<meta charset="utf-8">
<title>Cover Compare Quizzo UK – Home</title>
<link href="https://fonts.googleapis.com/css2?family=Source+Sans+3:wght@400;600;700&display=swap" rel="stylesheet">
<style>
:root{
  --orange:#f15a22;
  --teal:#0f8c7c;
  --teal-dark:#137a62;
  --band:#2a9e83;
  --blue:#2a8cb5;
  --sky:#1ea3c6;
  --green:#1e8a5e;
  --ink:#2c2c2c;
  --muted:#666;
  --line:#d9dcdc;
  --page:#eef3f4;
  --white:#fff;
}
*{box-sizing:border-box;margin:0;padding:0}
html,body{width:779px;height:1200px;overflow:hidden}
body{font-family:"Source Sans 3",Arial,sans-serif;font-weight:400;color:var(--ink);background:var(--page)}
.canvas{position:relative;width:779px;height:1200px;overflow:hidden;background:linear-gradient(#fff 0,#fff 230px,var(--page) 230px)}

/* header */
.hero-photo{position:absolute;left:300px;top:44px;width:340px;height:272px;
  background:radial-gradient(ellipse 46% 52% at 55% 45%,#b65a22 0,#c9763a 45%,#e3b48c 75%,rgba(255,255,255,0) 100%)}
.slash{position:absolute;left:0;top:0}
.brand{position:absolute;left:150px;top:18px;display:flex;align-items:center;gap:6px}
.brand-mark{width:26px;height:26px;background:var(--teal)}
.brand-name{font-weight:700;font-size:15px;line-height:14px;color:var(--teal);width:110px}
.nav{position:absolute;left:290px;top:22px;width:340px;height:26px;border-radius:13px;background:linear-gradient(#fff,#ececec);box-shadow:0 1px 2px rgba(0,0,0,.15);display:flex;overflow:hidden}
.nav a{flex:none;font-size:8px;color:#555;text-decoration:none;line-height:26px;text-align:center;white-space:nowrap;border-right:1px solid #ddd}
.nav a.is-active{background:var(--orange);color:#fff;font-weight:700}
.lookup-title{position:absolute;left:150px;top:98px;font-size:16px;font-weight:700;color:var(--teal)}
.select{position:absolute;left:150px;width:128px;height:19px;border:1px solid #c5d1d5;border-radius:3px;background:#eef3f6;font-size:7px;color:#888;padding:4px 8px;white-space:nowrap}
.select::after{content:"";position:absolute;right:7px;top:5px;border:4px solid transparent;border-top:5px solid #999}
.btn{position:absolute;left:150px;top:175px;width:70px;height:20px;border-radius:3px;background:var(--orange);color:#fff;font-size:7.5px;font-weight:700;text-align:center;line-height:20px}
.arrow{position:absolute;top:124px;width:15px;height:15px;border-radius:50%;background:#fff;box-shadow:0 0 2px rgba(0,0,0,.3)}
.arrow::after{content:"";position:absolute;top:4px;border:4px solid transparent}
.arrow.prev::after{left:2px;border-right:4px solid var(--orange)}
.arrow.next::after{left:6px;border-left:4px solid var(--orange)}

/* link strip */
.strip{position:absolute;left:0;top:230px;width:779px;height:77px;background:rgba(235,238,238,.82);border-top:1px solid var(--line);border-bottom:1px solid var(--line)}
.strip-item{position:absolute;top:9px;width:78px}
.strip-item h3{font-size:7.5px;font-weight:700;text-transform:uppercase;line-height:8px;margin-bottom:3px}
.strip-item p{font-size:6px;line-height:8.5px;color:#666}

/* main panel */
.panel{position:absolute;left:148px;top:318px;width:482px;height:752px;background:#fff;border-radius:5px;box-shadow:0 0 3px rgba(0,0,0,.06)}
.welcome{position:absolute;left:16px;top:16px;width:455px}
.welcome h1{font-size:19.5px;font-weight:700;color:var(--orange);margin-bottom:8px;white-space:nowrap}
.welcome p{font-size:7.5px;line-height:10px;margin-bottom:5px;color:#333}
.rule-h{position:absolute;left:0;top:123px;width:482px;border-top:1px solid #e3e6e6}
.rule-v{position:absolute;left:323px;top:124px;height:488px;border-left:1px solid #e3e6e6}
.news-title{position:absolute;left:15px;top:139px;font-size:13px;font-weight:400;color:var(--blue);white-space:nowrap}
.news{position:absolute;left:0;width:323px;height:107px}
.news .dash{position:absolute;left:28px;width:292px;border-top:1px dashed #bbb}
.date{position:absolute;left:-5px;top:2px;width:30px;height:40px;border-radius:0 20px 20px 0;background:var(--teal);color:#fff;text-align:center;padding-top:5px}
.date small{display:block;font-size:5.5px;line-height:6px}
.date b{display:block;font-size:11px;line-height:11px}
.news h2{position:absolute;left:30px;top:0;font-size:9px;font-weight:600;color:var(--orange);text-transform:uppercase;letter-spacing:.2px;white-space:nowrap}
.news p{position:absolute;left:30px;width:272px;font-size:6.2px;line-height:9px;color:#444}
.news .more{position:absolute;left:30px;top:58px;font-size:6.5px;color:var(--blue);text-decoration:underline;white-space:nowrap}
.shares{position:absolute;left:28px;top:81px;display:flex;gap:2px}
.shares i{width:14px;height:14px;border-radius:2px;display:block}
.pager{position:absolute;left:120px;top:600px;font-size:6.5px;color:var(--blue);display:flex;gap:8px;white-space:nowrap}

/* sidebar */
.ad{position:absolute;left:340px;top:138px;width:122px;height:121px;background:linear-gradient(#0b0b0d,#2c3340 60%,#111)}
.charity-avatar{position:absolute;left:343px;top:280px;width:34px;height:34px;border:2px solid var(--sky);background:linear-gradient(#a0552a,#d9a070)}
.charity-name{position:absolute;left:381px;top:282px;font-size:13px;line-height:12px;color:var(--sky);white-space:nowrap}
.charity-name span{display:block;font-size:9px}
.tweets{position:absolute;left:340px;top:322px;width:128px;height:112px;border-radius:8px;background:var(--sky);color:#fff;padding:14px 5px 0 6px}
.tweets p{font-size:5.5px;line-height:7px;font-weight:600}
.tweets .meta{font-weight:400;color:#d4f1f8;margin-bottom:4px;padding-bottom:3px;border-bottom:1px solid rgba(255,255,255,.4)}
.tweets .join{font-size:6.5px;margin-top:2px;font-weight:400}
.tweets .net{font-size:10px;font-weight:700}
.fbox{position:absolute;left:341px;top:460px;width:124px;height:134px;background:#333;border:1px solid #222;color:#fff;padding:4px}
.fbox .head{font-size:5px;font-weight:700;margin-bottom:3px}
.fbox .card{background:#fff;color:#333;font-size:5px;padding:3px;margin-bottom:3px;display:flex;gap:3px}
.fbox .sq{width:16px;height:16px;background:#3b5a98;flex:none}
.fbox .faces{display:flex;gap:2px;margin:3px 0}
.fbox .faces i{width:18px;height:18px;background:#8a9aa8;display:block}

/* reviews band */
.band{position:absolute;left:0;top:931px;width:779px;height:110px;background:var(--band)}
.foot{position:absolute;left:0;top:1040px;width:779px;height:160px;background:var(--teal-dark)}
.reviews{position:absolute;left:148px;top:931px;width:482px;height:139px;background:#fff;border-radius:0 0 5px 5px}
.review{position:absolute;top:14px;width:74px}
.review h3{font-size:8.5px;font-weight:700;margin-bottom:5px;white-space:nowrap}
.review p{font-size:6px;line-height:9.7px;color:#333;font-weight:400}
.review a{display:block;font-size:6px;line-height:9px;color:var(--blue);text-decoration:underline}
.footnav{position:absolute;left:15px;top:116px;font-size:6.5px;color:#555;white-space:nowrap}
.footnav span{color:#aaa;margin:0 5px}
.footshare{position:absolute;left:419px;top:113px;display:flex;gap:2px}
.footshare i{width:14px;height:14px;border-radius:2px;display:block}
.fcol{position:absolute;top:1086px;width:76px;color:#fff;font-size:6.5px;font-weight:400;line-height:9.5px;white-space:nowrap}
.fcol h4{font-size:7.5px;font-weight:700;line-height:10px}
.copy{position:absolute;left:160px;top:1181px;color:#fff;font-size:5.8px;white-space:nowrap}
</style>
</head>
<body>
<div class="canvas">

  <div class="hero-photo" role="img" aria-label="Photo of a brown and white spaniel puppy looking at the viewer"></div>
  <svg class="slash" width="779" height="240" aria-hidden="true">
    <polygon points="337,0 350,0 292,230 280,230" fill="#0f8c7c"/>
    <polygon points="352,0 362,0 304,230 296,230" fill="#bfe6e6"/>
  </svg>

  <div class="brand"><span class="brand-mark"></span><span class="brand-name">Cover Compare Quizzo UK</span></div>

  <nav class="nav">
    <a class="is-active" style="width:48px">Home</a><a style="width:36px">Policies</a><a style="width:44px">Glossary</a><a style="width:54px">Fact Sheets</a><a style="width:70px">Survey Reports</a><a style="width:88px;border:0">News &amp; Comment</a>
  </nav>

  <div class="lookup-title">Check out a policy</div>
  <div class="select" style="top:123px">Select company</div>
  <div class="select" style="top:149px">Select policy</div>
  <div class="btn">Find Policy</div>
  <span class="arrow prev" style="left:302px"></span>
  <span class="arrow next" style="left:623px"></span>

  <div class="strip">
    <div class="strip-item" style="left:149px"><h3 style="color:var(--green)">Policy Files</h3><p>Full policy details including type of vet fees cover and limits, ratings, age limits, excess details, benefits &amp; terms analysis</p></div>
    <div class="strip-item" style="left:234px"><h3 style="color:var(--blue)">Policy Search</h3><p>Exclusive to CCQ friends. Search our database of more than two hundred policies</p></div>
    <div class="strip-item" style="left:311px"><h3 style="color:var(--orange)">Fact Sheets</h3><p>Learn about pet insurance. A little knowledge is essential to choosing the right policy</p></div>
    <div class="strip-item" style="left:393px"><h3 style="color:var(--green)">Policy Listing (Type)</h3><p>Full lists of continuous policies (lifetime policies), 12 - month policies &amp; accident policies.</p></div>
    <div class="strip-item" style="left:478px"><h3 style="color:var(--blue)">Claims Survey</h3><p>Made a claim in the last 12 months? Please help us to help others by completing this 2-minute survey</p></div>
    <div class="strip-item" style="left:563px"><h3 style="color:var(--orange)">2013 Price Survey Report</h3><p>Due April 2013.</p></div>
  </div>

  <main class="panel">
    <section class="welcome">
      <h1>Welcome to Cover Compare Quizzo UK</h1>
      <p>This is an independent website dedicated to helping you to find the best pet insurance policy for your pet.</p>
      <p>Here you will find unbiased detailed information about almost all of the 205 pet insurance policies currently available in the UK (we hope the other 3 will follow shortly!)</p>
      <p>We do NOT sell any pet insurance policies nor do we receive commission from any insurance companies.</p>
    </section>
    <div class="rule-h"></div>
    <div class="rule-v"></div>

    <h2 class="news-title">Latest News &amp; Comment</h2>

    <article class="news" style="top:170px">
      <div class="dash" style="top:-5px"></div>
      <div class="date"><small>April</small><b>07</b><small>2013</small></div>
      <h2>Lorem ipsum dolor sit amet</h2>
      <p style="top:16px">Vestibulum ante ipsum primis in faucibus orci luctus et ultrices posuere cubilia Curae; In ac gravida purus. Nulla facilisi.</p>
      <p style="top:36px">Nullam id elit nibh. Duis ut dignissim tellus. Aliquam adipiscing pulvinar tempus. Vivamus vitae mi nec nisi euismod facilisis a vel neque. Mauris at elit et nisi gravida sollicitudin.</p>
      <span class="more">Read More »</span>
      <div class="dash" style="top:76px"></div>
      <div class="shares"><i style="background:#4fb3e3"></i><i style="background:#3b5a98"></i><i style="background:#1f6fa8"></i><i style="background:#6aa8d8"></i></div>
    </article>

    <article class="news" style="top:277px">
      <div class="dash" style="top:-5px"></div>
      <div class="date"><small>March</small><b>23</b><small>2013</small></div>
      <h2>Lorem ipsum dolor sit amet</h2>
      <p style="top:16px">Vestibulum ante ipsum primis in faucibus orci luctus et ultrices posuere cubilia Curae; In ac gravida purus. Nulla facilisi.</p>
      <p style="top:36px">Nullam id elit nibh. Duis ut dignissim tellus. Aliquam adipiscing pulvinar tempus. Vivamus vitae mi nec nisi euismod facilisis a vel neque. Mauris at elit et nisi gravida sollicitudin.</p>
      <span class="more">Read More »</span>
      <div class="dash" style="top:76px"></div>
      <div class="shares"><i style="background:#4fb3e3"></i><i style="background:#3b5a98"></i><i style="background:#1f6fa8"></i><i style="background:#6aa8d8"></i></div>
    </article>

    <article class="news" style="top:384px">
      <div class="dash" style="top:-5px"></div>
      <div class="date"><small>March</small><b>18</b><small>2013</small></div>
      <h2>Lorem ipsum dolor sit amet</h2>
      <p style="top:16px">Vestibulum ante ipsum primis in faucibus orci luctus et ultrices posuere cubilia Curae; In ac gravida purus. Nulla facilisi.</p>
      <p style="top:36px">Nullam id elit nibh. Duis ut dignissim tellus. Aliquam adipiscing pulvinar tempus. Vivamus vitae mi nec nisi euismod facilisis a vel neque. Mauris at elit et nisi gravida sollicitudin.</p>
      <span class="more">Read More »</span>
      <div class="dash" style="top:76px"></div>
      <div class="shares"><i style="background:#4fb3e3"></i><i style="background:#3b5a98"></i><i style="background:#1f6fa8"></i><i style="background:#6aa8d8"></i></div>
    </article>

    <article class="news" style="top:492px">
      <div class="dash" style="top:-5px"></div>
      <div class="date"><small>March</small><b>06</b><small>2013</small></div>
      <h2>Lorem ipsum dolor sit amet</h2>
      <p style="top:16px">Vestibulum ante ipsum primis in faucibus orci luctus et ultrices posuere cubilia Curae; In ac gravida purus. Nulla facilisi.</p>
      <p style="top:36px">Nullam id elit nibh. Duis ut dignissim tellus. Aliquam adipiscing pulvinar tempus. Vivamus vitae mi nec nisi euismod facilisis a vel neque. Mauris at elit et nisi gravida sollicitudin.</p>
      <span class="more">Read More »</span>
      <div class="dash" style="top:76px"></div>
      <div class="shares"><i style="background:#4fb3e3"></i><i style="background:#3b5a98"></i><i style="background:#1f6fa8"></i><i style="background:#6aa8d8"></i></div>
    </article>

    <div class="pager"><span>1</span><span>2</span><span>3</span><span>NEXT ›</span><span>LAST »</span></div>

    <div class="ad" role="img" aria-label="Advert poster for a pet adoption event with a dog and a cat in dark suits"></div>

    <div class="charity-avatar" role="img" aria-label="Profile photo of a spaniel puppy"></div>
    <div class="charity-name">PawAid Circle<span>PAWAID CIRCLE</span></div>
    <div class="tweets">
      <p>@Lorem ipsum dolor sit amet, consectetur adipiscing elit</p>
      <p class="meta">yesterday · reply · retweet · favorite</p>
      <p>@Nullam id elit nibh. Duis ut dignissim tellus #adipiscing #pulvinar</p>
      <p class="meta">yesterday · reply · retweet · favorite</p>
      <p class="join">Join the conversation</p>
      <p class="net">Chirpline</p>
    </div>

    <div class="fbox">
      <div class="head">Find us on Friendwall</div>
      <div class="card"><span class="sq"></span><b>Friendwall Builders</b></div>
      <div class="card" style="height:44px"><span class="sq"></span><span><b>Friendwall Builders</b><br>Join us for a day of building with our community team.</span></div>
      <div style="font-size:5px">1,475 people like this</div>
      <div class="faces"><i></i><i></i><i></i><i></i><i></i></div>
      <div style="font-size:5px">Friendwall social plugin</div>
    </div>
  </main>

  <div class="band"></div>
  <div class="foot"></div>
  <section class="reviews">
    <div class="review" style="left:13px"><h3 style="color:var(--orange)">Review Num 1</h3><p>Lorem ipsum dolor sit amet, consectetur adipiscing elit. Donec id augue in nulla venenatis sollicitudin. Donec scelerisque imperdiet.</p><a>Read More</a></div>
    <div class="review" style="left:91px"><h3 style="color:var(--teal)">Lorem 2</h3><p>Vestibulum ante ipsum primis in faucibus orci luctus et ultrices posuere cubilia Curae. In ac gravida purus. Cras arcu erat rah melio.</p><a>Read More</a></div>
    <div class="review" style="left:169px"><h3 style="color:var(--blue)">Ipsum Dolor 3</h3><p>Lorem ipsum dolor sit amet, consectetur adipiscing elit. Donec id augue in nulla venenatis sollicitudin. Donec scelerisque imperdiet.</p><a>Read More</a></div>
    <div class="review" style="left:247px"><h3 style="color:var(--orange)">Sit Amet 4</h3><p>Vestibulum ante ipsum primis in faucibus orci luctus et ultrices posuere cubilia Curae. In ac gravida purus. Cras arcu erat rah melio.</p><a>Read More</a></div>
    <div class="review" style="left:325px"><h3 style="color:var(--teal)">Consectetur 5</h3><p>Lorem ipsum dolor sit amet, consectetur adipiscing elit. Donec id augue in nulla venenatis sollicitudin. Donec scelerisque imperdiet.</p><a>Read More</a></div>
    <div class="review" style="left:403px"><h3 style="color:var(--teal)">Adipiscing Elit 6</h3><p>Vestibulum ante ipsum primis in faucibus orci luctus et ultrices posuere cubilia Curae. In ac gravida purus. Cras arcu erat rah melio.</p><a>Read More</a></div>
    <nav class="footnav">Home<span>|</span>Policies<span>|</span>Glossary<span>|</span>Fact Sheets<span>|</span>Survey Reports<span>|</span>News &amp; Comment</nav>
    <div class="footshare"><i style="background:#4fb3e3"></i><i style="background:#3b5a98"></i><i style="background:#1f6fa8"></i></div>
  </section>

  <div class="fcol" style="left:161px"><h4>Lorem ipsum</h4>Dolor sit amet elitosa<br>Consect Eturitalu<br>Adipiscing<br>Donec id augue<br>In nulla<br>Donec scelerisque<br>Imperiet</div>
  <div class="fcol" style="left:239px"><h4>Nullam id nibh</h4>Duis ut<br>Dignissim tellus<br>Aliquam ara<br>Pulvinar tempus<br>Vivamus vita<br>Mi nec nisi<br>Euismod facilisis</div>
  <div class="fcol" style="left:317px"><h4>Lorem ipsum</h4>Mauris at elitilet nisis<br>Gravida sollici<br>Suspendisse sit ametu<br>Magna<br>Nam dignissim<br>Lacus males<br>Fermentum</div>
  <div class="fcol" style="left:395px"><h4>Nullam id elit</h4>Duis ut<br>Dignissim<br>Aliquam<br>Pulvinar tempus<br>Vivamus vitae<br>Mi nec nisi<br>Euismod facilisis</div>
  <div class="fcol" style="left:473px"><h4>Id elit nibh</h4>Duis ut<br>Dignissim tellus<br>Aliquam adipiscing<br>Pulvinar tempus<br>Vivamus<br>Mi nec nisi<br>Euismod</div>
  <div class="fcol" style="left:551px"><h4>Lorem ipsum</h4>Dolor sit amet elitosa<br>Consect<br>Adipiscing<br>Donec id augue<br>In nulla venenatis<br>Donec sceleri<br>Imperiet iaculis</div>

  <div class="copy">© Copyright 2013 Cover Compare Quizzo &nbsp;|&nbsp; Privacy Policy &nbsp;|&nbsp; Legal</div>
</div>
</body>
</html>
```